Bref créative
Bellwether Rheumatology Associates
The Institute for Bone Density
I need double sided standard sized Business Card [3.5" x 2"]
We are flexible, can use different font if looks good.
Professional
Daniel P. Hurlow, MD
Harborview Lakes Medical Center
2716 Kelmont Avenue, Suite 430
Miami Beach, FL 33187
dhurlow1982@mailbrook.example
We are presently a group of two rheumatologists. We are expecting a third rheumatologist the summer of 2012. We will need two versions, one that has my name, Daniel P. Hurlow, MD, and the other that has my partner's name Tomas L. Ferreira Vidal, MD. We are striving for a modern, clean, professional, corporate look. Please use the logo that we are providing. Will be uploading. Would like to keep colors simple. As per logo, we use dark red and gray; I suppose the text on the card will need to be black or similar. Please do NOT put email on card. We still do not have an "official" email. Will also like to see letterhead and envelope design, as well. With the envelope, we are simply looking for a neat-looking, recognizable return address section.
The back of the business card should be the appointment reminder section. Should have a blank for 1. Patient name, 2. Date of appointment 3. Time of appointment 4. Day of week that we can circle (mon-fri only) 5. check box for doctor (either Daniel P. Hurlow, MD or Tomas L. Ferreira Vidal).
Here is the logo.

```html
<!DOCTYPE html>
<html lang="en">
<head>
<meta charset="utf-8">
<title>Bellwether Rheumatology Associates — Stationery</title>
<link href="https://fonts.googleapis.com/css2?family=Open+Sans:wght@400;600;700&display=swap" rel="stylesheet">
<style>
  :root {
    --backdrop: #a8a8a8;
    --paper: #ffffff;
    --brand-red: #6b1c22;
    --brand-gray: #7b7b7b;
    --ink: #2a2a2a;
    --rule: #bdbdbd;
  }
  * { box-sizing: border-box; margin: 0; padding: 0; }
  html, body { width: 1200px; height: 626px; overflow: hidden; }
  body {
    background: var(--backdrop);
    font-family: "Open Sans", Arial, sans-serif;
    color: var(--ink);
    position: relative;
  }
  .sheet {
    position: absolute;
    background: var(--paper);
    box-shadow: 0 1px 3px rgba(0,0,0,0.25);
  }
  .brand {
    display: flex;
    flex-direction: column;
    align-items: center;
    text-align: center;
    color: var(--brand-red);
  }
  .brand-mark {
    width: 16px; height: 16px;
    background: var(--brand-red);
    margin-bottom: 4px;
  }
  .brand-name {
    font-weight: 600;
    text-transform: uppercase;
    letter-spacing: 0.04em;
    line-height: 1.15;
    font-size: 12px;
  }
  .brand-sub {
    font-weight: 600;
    text-transform: uppercase;
    letter-spacing: 0.04em;
    font-size: 6px;
    margin-top: 2px;
    padding-top: 2px;
    border-top: 1px solid var(--brand-red);
  }
  .contact-footer {
    position: absolute;
    left: 0; right: 0;
    text-align: center;
    font-size: 5.5px;
    line-height: 1.6;
    color: var(--ink);
  }
  .contact-footer b { font-weight: 700; }

  /* Appointment card (back) */
  .card-back { left: 34px; top: 230px; width: 182px; height: 106px; padding: 12px 14px; }
  .appt-title { font-size: 7px; font-weight: 700; color: var(--brand-red); margin-bottom: 9px; }
  .appt-row { display: flex; align-items: flex-end; font-size: 5.5px; margin-bottom: 8px; gap: 4px; }
  .appt-row .blank { flex: 1; border-bottom: 1px solid var(--rule); height: 6px; }
  .appt-days { display: flex; gap: 8px; font-size: 5.5px; margin-bottom: 7px; }
  .appt-doctors { display: flex; gap: 10px; font-size: 5.5px; }
  .check { display: inline-block; width: 5px; height: 5px; border: 1px solid var(--ink); margin-right: 3px; vertical-align: middle; }

  /* Business card (front) */
  .card-front { left: 34px; top: 355px; width: 182px; height: 101px; }
  .card-front .brand { margin-top: 14px; }
  .card-front .brand-mark { width: 10px; height: 10px; margin-bottom: 3px; }
  .card-front .brand-name { font-size: 7px; }
  .card-front .brand-sub { font-size: 4px; }
  .card-person { text-align: center; font-size: 6px; font-weight: 700; margin-top: 6px; }
  .card-front .contact-footer { bottom: 8px; font-size: 4px; }

  /* Letterhead */
  .letterhead { left: 293px; top: 24px; width: 384px; height: 571px; }
  .letterhead .brand { margin-top: 16px; }
  .letterhead .contact-footer { bottom: 18px; }

  /* Envelope back */
  .envelope-back { left: 689px; top: 77px; width: 473px; height: 211px; }
  .envelope-flap { position: absolute; left: 0; top: 0; width: 100%; height: 60px; }

  /* Envelope front */
  .envelope-front { left: 689px; top: 336px; width: 473px; height: 221px; }
  .envelope-front .brand { position: absolute; left: 140px; top: 22px; width: 200px; }
  .envelope-front .contact-footer { left: 180px; right: 20px; top: 172px; }
</style>
</head>
<body>

  <section class="sheet card-back" aria-label="Appointment reminder card">
    <p class="appt-title">Appointment Reminder</p>
    <div class="appt-row"><span>Patient Name:</span><span class="blank"></span></div>
    <div class="appt-row"><span>Date of Appointment:</span><span class="blank"></span><span>Time of Appointment:</span><span class="blank"></span></div>
    <div class="appt-days"><span>Mon</span><span>Tue</span><span>Wed</span><span>Thu</span><span>Fri</span></div>
    <div class="appt-doctors">
      <span><span class="check"></span>Dr. Hurlow</span>
      <span><span class="check"></span>Dr. Ferreira Vidal</span>
    </div>
  </section>

  <section class="sheet card-front" aria-label="Business card">
    <div class="brand">
      <span class="brand-mark"></span>
      <span class="brand-name">Bellwether<br>Rheumatology Associates</span>
      <span class="brand-sub">The Institute for Bone Density</span>
    </div>
    <p class="card-person">Daniel P. Hurlow, MD</p>
    <p class="contact-footer">
      <b>Phone:</b> (305) 555-0148 | <b>Fax:</b> (305) 555-0149<br>
      Harborview Lakes Medical Center, 2716 Kelmont Avenue, Suite 430, Miami Beach, FL 33187
    </p>
  </section>

  <section class="sheet letterhead" aria-label="Letterhead">
    <div class="brand">
      <span class="brand-mark"></span>
      <span class="brand-name">Bellwether<br>Rheumatology Associates</span>
      <span class="brand-sub">The Institute for Bone Density</span>
    </div>
    <p class="contact-footer">
      <b>Phone:</b> (305) 555-0148 | <b>Fax:</b> (305) 555-0149<br>
      <b>Address:</b> Harborview Lakes Medical Center, 2716 Kelmont Avenue, Suite 430, Miami Beach, FL 33187
    </p>
  </section>

  <section class="sheet envelope-back" aria-label="Envelope back">
    <svg class="envelope-flap" viewBox="0 0 473 60" preserveAspectRatio="none">
      <path d="M0 2 L18 52 Q22 58 30 58 L443 58 Q451 58 455 52 L473 2" fill="none" stroke="#e2e2e2" stroke-width="1"/>
    </svg>
  </section>

  <section class="sheet envelope-front" aria-label="Envelope front">
    <div class="brand">
      <span class="brand-mark"></span>
      <span class="brand-name">Bellwether<br>Rheumatology Associates</span>
      <span class="brand-sub">The Institute for Bone Density</span>
    </div>
    <p class="contact-footer">
      <b>Phone:</b> (305) 555-0148 | <b>Fax:</b> (305) 555-0149<br>
      <b>Address:</b> Harborview Lakes Medical Center, 2716 Kelmont Avenue, Suite 430, Miami Beach, FL 33187
    </p>
  </section>

</body>
</html>
```